webpage design for www.brightpathYOU.com

Hi-
I am creating a website about weight loss through healthy eating. The target audience is 80% women, of all races and ethnic backgrounds, in the 35-55 age range, all of whom are overweight and want to lose weight.
At first (which is where you come in), the website will be strictly informational, and products for sale will be added later.
Obviously not all of the following information can be incorporated into the design, but to give you some background, here is what I am doing.
First thing the site visitor needs to know is what the website is about. It’s about them, and how they can lose weight effectively. It’s only secondarily about me, and the w
ebsite must talk about me only from the point of view of how can I help them. It is your job to create a webpage where I can do just that. I have the content of this page ready to go, but I need you to create a beautiful, enticing, and effective framework to put it all in. You do not need to enter any copy except for the small amount noted below.
My clients are looking for a weight loss method or program that is effective, healthy, and long-lasting. This system addresses those needs. It's important for the clients to know that with the brightpathYOU system, there is no hunger, no deprivation, no pills, no weighing foods or calorie counting, no special products to buy, among other things.
And not only does the weight come off, but there are other health benefits as well. The brightpathYOU system can lower cholesterol, blood pressure, dependence on insulin for type 2 diabetics, reduce risk of heart disease and certain types of cancer, among other things-and this has been medically documented.
When I say "healthy eating", the focus of this program is on vegetables, fruits, and grains, with no added fat, but I do not want the main page to highlight that, since the whole notion of lots of veggies can scare people away. Pictures of fruits and veggies are fine. I'll introduce scary words like “vegan” and “no added fat” into the written materials and in the video, but there is no point in chasing people away too quickly!
The banner headline should have incorporated into it, in addition to the business name, the following: "Lose weight...improve your looks...improve your health...transform your life". You will need to choose a typeface and add this copy.
I would like to have a collage of healthy, happy, slender people of all ages (mostly women), in group and social settings-but not all exercising or doing yoga or jogging, since many of my target audience are couch potatoes (at least right now). If you do use any pictures of overweight people, they should be solitary, not part of a group, and definitely not looking happy!. I was thinking of having this only in the banner at top, but if you find a way to make the site attractive by adding a thin border with this as well, feel free.
Or, since I am not a design person by any stretch of the imagination, if you have another idea as to the banner design and the rest, I am certainly open to it.
In addition to the banner headline, I want a two-column design on the lower section, one being a narrower sidebar on the right, with a place for the customer to enter his/her name, and the following: Free video & eBook" "Every Plate Tells A Story, Every Meal Builds A Habit-And How You Can Shape Yours Today", and they get this in exchange for entering their first and last name, and email address. I can link this to AWeber later. I have a video widget, as well as a bunch more, in place, so you do not need to create or order those.
I will later add something to this section about no spam will be sent.
Below that in the same thinner column on the right should be an archives section, which you will need to create if the Wordpress theme doesn't have it already. This should be the same on all pages, except the single column pages, and since they will have sales pitches, should not have anything else.
The wider, main column I want to have three particular areas: One, is video. Two is text. Three is comments.
I will be using a LOT of video, but below each video I want to be able to place the text for the video (not everyone wants to watch a video), I want a static first page, but no comments section on the first page (I may want to add a comments section later, but not now).
The next page will be a basic "about me" page. This will be a video with text below in the main section, and will have the same enter your email info on the right side bar. No need to have "comments" below this. I've uploaded a picture of me, which should appear on this page, as well as on the main page.
Then will be a blog page, again the same layout: videos, which I can add to consecutively, with "comments" below, (which I can approve or disapprove before they get posted), with the offer in the right sidebar. Any videos will also show up in the archives section.
And a "recipes" page, video and text, plus comments section, with the email offer in the sidebar. These will show up as an archives section as well. I’ll add recipes and cooking videos later.
Then will be a "Products" page, which will for now be blank (I haven't created them yet), but with the email offer in the right side bar. No comments section to this one.
And a Contact Us page, no comments section either. I'll add the contact information later.
Across bottom of each page, perhaps in a somewhat contrasting color, will be a disclaimer, which I’ll need to be able to edit. This will be in small print, and should say something like, “This website expresses the opinions of the author, is intended for informational and educational purposes only, should not be construed as medical or dietary advice, and is not intended to be a substitute for same. Before changing diets, medications, or before undertaking a weight loss regimen, be sure to consult with your physician. This information is not intended to diagnose or treat any illness or health problems you may be experiencing, so kindly address your doctor with these concerns.” You can copy and paste this text.
Each page should also say “copyright 2014, Ned Brook”, which you will need to add.
Beyond that I will need single blank column pages which I will later make into landing, thank you, and so on pages. This will not be visible from the main page, though.

This will be done in Wordpress. I have the URL and the page is set up on Wordpress already, but I will need you to integrate the design into my Wordpress site when it is completed, so you will need a working knowledge of Wordpress. So the final winner will need to have the capability of coding the design and uploading it into my website and server. When you are done, it will be a complete and turnkey website, and all I have to do is add the copy and videos.

I am not particular as to a Wordpress theme, as long as it's an unpaid one, but if you find a paid one that you think is useable and needs to be paid for, let me know so I can check it out.
And I will need to be easily able to change and edit anything in the webpage on Wordpress at the end, after you are finished, with NO HTML, so any theme must be dummy friendly (I am the dummy, by the way!). (I have a basic familiarity with Wordpress, but none of HTML.)

Hopefully this gives you more than enough information to work with. Even though this page is a bit complicated, the actual website should be pretty simple looking, not busy or full of distractions, with only a few focal points.
Updates

Hi-information has been updated, I've changed my status to "committed", and I've uploaded a lot of pictures of fruit and veggies for you to use.  Thanks for your attention!
Ned

Target Market(s)

As stated above, "The target audience is 80% women, of all races and ethnic backgrounds, in the 35-55 age range, all of whom are overweight and want to lose weight."

Industry/Entity Type

Cooking

Font styles to use
Serif

Requirements
Must have
• The home page serves two purposes: one, to introduce the reader to the material, but two, and equally important, to build my email list. To that end, the opt in form on the right should say prominently, Free video & eBook" "Every Plate Tells A Story, Every Meal Builds A Habit-And How You Can Shape Yours Today", and below that should be the opt in boxes.
The banner can be scrolling, to attract ATTENTION, should lead to the ACTION of watching the video, which will have in it a CALL TO ACTION of signing up for the hopefully compelling OFFER of the free ebook and video-and of course the newsletter. My purpose on page one is to directly address the question of "What's in it for me?", and then to deliver with the video and ebook offer.
I've uploaded a bunch of pictures of veggies and fruit-feel free to use them, as they are all mine.
Possibly a scrolling banner could be used with alternating pictures of happy, slender people alternating with pictures, and the captions of "lLose weight...improve your looks...improve your health...transform your life"

Emphasis should be on healthy eating, not on pounds lost or measuring one's waist or some such thing.

Banner headline should include: ""Lose weight...improve your looks...improve your health...transform your life"
Should not have
• Please avoid pictures of picture-perfect people, scales, and so on-I do not want this to be some generic, cookie-cutter weight loss web site. This is about weight loss from a different point of view-and I don't think this will come across in the webpage, but the concept will be introduced later. It's about weight loss as a byproduct of changing eating habits from unhealthy to healthy.

```html
<!DOCTYPE html>
<html lang="en">
<head>
<meta charset="utf-8">
<title>brightpathYOU</title>
<link rel="stylesheet" href="https://fonts.googleapis.com/css2?family=Titillium+Web:wght@300;400&family=Arimo:wght@400&display=swap">
<style>
  :root {
    --cream: #f0e6df;
    --brown: #8b6240;
    --berry: #960d40;
    --berry-dark: #8a0f2a;
    --field: #d8b1b9;
    --hero-red: #8e0a12;
    --hero-dark: #3a0306;
    --frame: #dcdfe2;
    --player: #2b2b2b;
    --ink: #222;
    --dot: #4a4d52;
    --dot-active: #990a0a;
    --social: #8b6240;
  }
  * { box-sizing: border-box; margin: 0; padding: 0; }
  html, body { width: 1029px; height: 1200px; overflow: hidden; background: #fff; }
  body { position: relative; font-family: "Titillium Web", sans-serif; color: var(--ink); }
  .abs { position: absolute; }

  /* brand */
  .brand { display: flex; align-items: center; color: var(--brown); font-weight: 400; line-height: 1; white-space: nowrap; }
  .brand-mark { display: block; background: var(--brown); border-radius: 3px; }
  .header-brand { left: 21px; top: 17px; height: 36px; font-size: 31px; gap: 9px; }
  .header-brand .brand-mark { width: 35px; height: 35px; }
  .footer-brand { left: 16px; top: 1041px; height: 28px; font-size: 24px; gap: 7px; }
  .footer-brand .brand-mark { width: 27px; height: 27px; }

  /* header */
  .site-header { left: 0; top: 0; width: 1029px; height: 71px; background: var(--cream); }
  .main-nav { right: 22px; top: 22px; font-size: 19px; font-weight: 300; line-height: 26px; color: var(--brown); display: flex; gap: 9px; }

  /* hero */
  .hero { left: 0; top: 71px; width: 1029px; height: 319px;
    background: radial-gradient(ellipse at 55% 45%, #a40d14 0%, var(--hero-red) 45%, #5a0509 80%, var(--hero-dark) 100%);
    border-top: 3px solid #111; }
  .hero-photo { left: 0; top: 74px; width: 357px; height: 316px;
    background: linear-gradient(180deg, #d9ccc3 0%, #ebe4de 100%); }
  .produce-left { left: 8px; top: 341px; width: 212px; height: 142px; border-radius: 10px;
    background: linear-gradient(180deg, #c99a4a 0%, #a9814f 100%); opacity: .85; }
  .produce-basket { left: 315px; top: 323px; width: 260px; height: 149px; border-radius: 10px;
    background: linear-gradient(180deg, #7d8a4a 0%, #a4603e 100%); opacity: .85; }
  .hero-copy { left: 411px; top: 138px; color: #fff; font-weight: 300; line-height: 1; white-space: nowrap; }
  .hero-copy .line-lead { font-size: 64px; }
  .hero-copy .line-mid { font-size: 28px; margin-top: 6px; }
  .hero-copy .line-end { font-size: 48px; margin-top: 14px; }
  .slider-dots { left: 913px; top: 413px; display: flex; gap: 3px; }
  .slider-dots i { width: 13px; height: 13px; background: var(--dot); }
  .slider-dots i.active { background: var(--dot-active); }

  /* video */
  .video-frame { left: 29px; top: 511px; width: 445px; height: 329px; background: var(--frame); border-radius: 9px; }
  .player { left: 41px; top: 522px; width: 421px; height: 307px; background: var(--player); border-radius: 5px; }
  .video-still { left: 47px; top: 534px; width: 411px; height: 245px;
    background: linear-gradient(180deg, #dfe3dc 0%, #cdd3c8 100%); }
  .player-controls { left: 47px; top: 784px; width: 411px; height: 40px; }

  .intro-text { left: 31px; top: 864px; width: 462px; font-family: "Arimo", sans-serif; font-size: 14.5px; line-height: 18px; color: var(--ink); }
  .learn-more { left: 31px; top: 933px; font-family: "Arimo", sans-serif; font-size: 15px; color: var(--berry-dark); }

  /* opt-in */
  .optin { left: 549px; top: 511px; width: 450px; height: 442px; background: var(--berry); border-radius: 8px; color: #fff; }
  .optin-title { position: absolute; left: 28px; top: 30px; font-size: 42px; font-weight: 300; line-height: 54px; white-space: nowrap; }
  .optin-sub { position: absolute; left: 29px; top: 90px; width: 400px; font-size: 19.5px; line-height: 25px; font-weight: 300; }
  .field { position: absolute; left: 25px; width: 386px; height: 40px; background: var(--field); border-radius: 6px;
    color: var(--berry-dark); font-size: 20px; font-weight: 300; line-height: 40px; padding: 0 19px; }
  .optin-btn { position: absolute; left: 26px; top: 340px; width: 221px; height: 51px; background: var(--cream); border-radius: 6px;
    color: var(--berry-dark); font-size: 20px; font-weight: 300; display: flex; align-items: center; justify-content: center; }

  /* footer */
  .site-footer { left: 0; top: 1010px; width: 1029px; height: 119px; background: var(--cream); }
  .copyright { left: 16px; top: 1079px; font-family: "Arimo", sans-serif; font-size: 11px; color: var(--brown); }
  .footer-nav { left: 348px; top: 1037px; display: flex; gap: 12px; font-family: "Arimo", sans-serif; font-size: 15px; color: var(--brown); }
  .social { top: 1033px; width: 25px; height: 25px; background: var(--social); }
  .like-box { top: 1070px; height: 18px; border: 1px solid #c9c3bd; background: #f7f4f1; border-radius: 2px; }

  .disclaimer { left: 0; top: 1144px; width: 1029px; text-align: center; font-family: "Arimo", sans-serif; font-size: 10.5px; line-height: 12.5px; color: #333; }
</style>
</head>
<body>

<header class="site-header abs"></header>
<div class="brand header-brand abs"><span class="brand-mark"></span><span>brightpathYOU</span></div>
<nav class="main-nav abs">
  <span>home</span><span>|</span><span>about us</span><span>|</span><span>what we do</span><span>|</span><span>contact us</span>
</nav>

<section class="hero abs"></section>
<div class="hero-photo abs" role="img" aria-label="Smiling woman eating a green salad"></div>
<div class="produce-left abs" role="img" aria-label="Pile of fresh fruit: bananas, melon, grapes and berries"></div>
<div class="produce-basket abs" role="img" aria-label="Basket of fresh vegetables and tomatoes"></div>
<div class="hero-copy abs">
  <div class="line-lead">Lose weight...</div>
  <div class="line-mid">improve your looks...improve your health...</div>
  <div class="line-end">transform your life</div>
</div>
<div class="slider-dots abs"><i></i><i></i><i class="active"></i><i></i><i></i></div>

<div class="video-frame abs"></div>
<div class="player abs"></div>
<div class="video-still abs" role="img" aria-label="Video still of a woman at an open fridge full of fresh food"></div>
<svg class="abs" style="left:207px;top:617px" width="90" height="90" viewBox="0 0 90 90">
  <circle cx="45" cy="45" r="41" fill="none" stroke="#fff" stroke-width="4"/>
  <path d="M35 27 L64 45 L35 63 Z" fill="#fff"/>
</svg>
<svg class="player-controls abs" viewBox="0 0 411 40">
  <rect x="0" y="0" width="411" height="6" fill="#555"/>
  <circle cx="6" cy="3" r="6" fill="#ddd"/>
  <rect x="19" y="17" width="4" height="12" fill="#bbb"/><rect x="26" y="17" width="4" height="12" fill="#bbb"/>
  <path d="M58 20 h5 l6 -5 v16 l-6 -5 h-5 z" fill="#bbb"/>
  <text x="86" y="28" font-family="Arimo, sans-serif" font-size="10" fill="#fff">00:00 <tspan fill="#aaa">/ 18:50</tspan></text>
  <circle cx="282" cy="23" r="6" fill="none" stroke="#bbb" stroke-width="3"/>
  <circle cx="309" cy="23" r="5" fill="#bbb"/>
  <rect x="322" y="18" width="14" height="10" fill="none" stroke="#fff" stroke-width="2"/>
  <rect x="348" y="18" width="16" height="10" fill="none" stroke="#bbb" stroke-width="2"/>
  <path d="M376 16 h5 M376 16 v5 M394 16 h-5 M394 16 v5 M376 30 h5 M376 30 v-5 M394 30 h-5 M394 30 v-5" stroke="#bbb" stroke-width="2"/>
</svg>

<p class="intro-text abs">Ut wisi enim ad minim veniam, quis nostrud exerci tation ullamcorper suscipit lobortis nisl ut aliquip ex ea commodo consequat. Duis autem vel eum iriure dolor in hendrerit in vulputate velit esse molestie.</p>
<div class="learn-more abs">Learn more »</div>

<section class="optin abs">
  <div class="optin-title">Free Video &amp; eBook</div>
  <div class="optin-sub">Every Plate Tells A Story, Every Meal Builds A Habit-And How You Can Shape Yours Today</div>
  <div class="field" style="top:175px">first name</div>
  <div class="field" style="top:226px">last name</div>
  <div class="field" style="top:279px">email address</div>
  <div class="optin-btn">Get Free eBook Now</div>
</section>

<footer class="site-footer abs"></footer>
<div class="brand footer-brand abs"><span class="brand-mark"></span><span>brightpathYOU</span></div>
<div class="copyright abs">© 2014 brightpathYOU. All Rights Reserved</div>
<nav class="footer-nav abs"><span>Home</span><span>About Us</span><span>What We Do</span><span>Contact Us</span><span>Terms</span><span>Privacy</span></nav>
<span class="social abs" style="left:872px"></span>
<span class="social abs" style="left:911px"></span>
<span class="social abs" style="left:951px"></span>
<span class="like-box abs" style="left:874px;width:46px"></span>
<span class="like-box abs" style="left:925px;width:31px"></span>

<div class="disclaimer abs">
  Disclaimer: Lorem ipsum dolor sit amet, consectetur adipisicing elit, sed do eiusmod tempor incididunt ut labore<br>
  et dolore magna aliqua. Ut enim ad minim veniam, quis nostrud exercitation ullamco laboris nisi ut aliquip ex ea commodo consequat. Duis aute irure dolor in reprehenderit in<br>
  voluptate velit esse cillum dolore eu fugiat nulla pariatur. Excepteur sint occaecat cupidatat non proident, sunt in culpa qui officia deserunt mollit anim id est laborum.
</div>

</body>
</html>
```